Chorkonzert Thema Die KlangKiesel fällt aus dem Rahmen
Zielgruppe
Wir sind ein A-Capella Chor 'KlangKiesel'. Wir wollen Jung und Alt ansprechen.
Es sollen Plakate (30x42 cm) und Handzettel erstellt werden.
Aufgabenstellung
Wir sind noch völlig offen. Beim letzten Konzert wurde ein Foto (mit allen verwendet)
Entweder könnte wieder ein Foto mitverarbeitet werden. Wir laden mal zwei drei Fotos hoch. Von den Einzelstimmen sind jeweils Bilder noch vorhanden. Würden aber auch spezielle Fotos machen lassen je nachdem.
Gerne ein Plakat das entsprechend dem Konzerttitel etwas aus dem Rahmen fällt.
Text:
Wann: 10. und 12.03.2017 um ? Uhr
Eintritt: 8 Euro VVK 10 Euro AK
Kartenbestellung

```html
<!DOCTYPE html>
<html lang="de">
<head>
<meta charset="utf-8">
<title>KlangKiesel – acapella chor</title>
<link rel="stylesheet" href="https://fonts.googleapis.com/css2?family=Lobster&display=swap">
<style>
  :root {
    --poster-orange: #E8521E;
    --ornament-yellow: #F5AE35;
    --ornament-soft: rgba(245, 174, 53, 0.55);
    --type-white: #FFFFFF;
    --type-shadow: #B8321A;
  }
  html, body {
    margin: 0;
    padding: 0;
    overflow: hidden;
    background: var(--poster-orange);
  }
  .poster {
    position: relative;
    width: 856px;
    height: 1200px;
    background: var(--poster-orange);
    overflow: hidden;
    font-family: "Lobster", cursive;
    color: var(--type-white);
  }
  .ornament {
    position: absolute;
    left: 20px;
    top: 90px;
    width: 790px;
    height: 830px;
    border-radius: 50%;
    background: radial-gradient(circle at 50% 50%,
      var(--ornament-yellow) 0%,
      var(--ornament-soft) 45%,
      rgba(245, 174, 53, 0) 72%);
  }
  .shadowed {
    position: absolute;
    margin: 0;
    font-weight: 400;
    line-height: 1;
    white-space: nowrap;
    text-shadow: 4px 4px 0 var(--type-shadow);
  }
  .choir-name {
    left: 36px;
    top: 292px;
    font-size: 142px;
    letter-spacing: -1px;
  }
  .choir-tagline {
    left: 345px;
    top: 462px;
    font-size: 70px;
  }
  .concert-dates {
    left: 345px;
    top: 780px;
    font-size: 74px;
    letter-spacing: -1px;
  }
  .concert-time {
    right: 54px;
    top: 866px;
    font-size: 42px;
  }
  .event-details {
    position: absolute;
    left: 0;
    right: 0;
    top: 992px;
    text-align: center;
  }
  .venue, .prices, .booking {
    margin: 0;
    font-weight: 400;
    line-height: 1;
    white-space: nowrap;
  }
  .venue {
    font-size: 42px;
  }
  .prices {
    margin-top: 22px;
    font-size: 44px;
  }
  .booking {
    margin-top: 22px;
    font-size: 21px;
  }
</style>
</head>
<body>
  <main class="poster">
    <div class="ornament" role="img" aria-label="Dekoratives Ornament aus vier gelben Spiralen mit schwebenden Musiknoten"></div>

    <h1 class="shadowed choir-name">KlangKiesel</h1>
    <p class="shadowed choir-tagline">acapella chor</p>

    <p class="shadowed concert-dates">10.+12.03.2017</p>
    <p class="shadowed concert-time">20.00h</p>

    <section class="event-details">
      <p class="venue">Aula Lindenhof Gymnasium</p>
      <p class="prices">Karten: Vvk 8 €, Ak 10 €</p>
      <p class="booking">Kartenbestellung Tel. 07531 - 48210&nbsp;&nbsp;email: odile.wach@post.de</p>
    </section>
  </main>
</body>
</html>
```